In Search of a FANTASTIC BUSINESS CARD REFRESH AND REDESIGN

I would like to redesign the current business card for my company.  There is a parent company, Brookfane Care Group, with 2 operating companies - Brookfane Homecare and Brookfane Senior Living.
I will include the current business card design, along with the 3 logos I would like incorporated.  The business card can be two sided.  I'm looking for something clean, professional, and a fresh new look.

Target Market(s)
Hospitals, social workers, insurance agents, family members of seniors
Industry/Entity Type
Healthcare
Contact Information for Business Card
Name, title of person, address, phone number, web address, email address
Look and feel
Each slider illustrates characteristics of the customer's brand and the style your logo design should communicate.

```html
<!DOCTYPE html>
<html lang="en">
<head>
<meta charset="utf-8">
<title>Brookfane Care Group – Business Card</title>
<link rel="stylesheet" href="https://fonts.googleapis.com/css2?family=Poppins:wght@400;500;600;700&family=Crimson+Text:ital@1&display=swap">
<style>
  :root {
    --bg: #1c1c1c;
    --card-white: #ffffff;
    --ink: #111111;
    --ink-soft: #333333;
    --band: #151515;
    --coral: #ee7b7f;
    --teal: #4f9b95;
    --back-dark: #0d0d0d;
    --back-mid: #2a2a2a;
    --back-light: #b9b9b9;
  }
  * { box-sizing: border-box; margin: 0; padding: 0; }
  html, body { width: 1200px; height: 1108px; overflow: hidden; background: var(--bg); }
  .stage { position: relative; width: 1200px; height: 1108px; }

  .card {
    position: absolute; top: 204px; width: 400px; height: 700px;
    border-radius: 28px; overflow: hidden;
  }
  .card--front { left: 170px; background: var(--card-white); }
  .card--back { left: 630px; background: var(--back-dark); }

  .brand {
    position: absolute; top: 92px; left: 0; right: 0;
    display: flex; flex-direction: column; align-items: center;
  }
  .brand__mark { width: 70px; height: 70px; background: var(--ink); border-radius: 8px; margin-bottom: 18px; }
  .brand__name {
    font-family: "Poppins", sans-serif; font-weight: 600; color: var(--ink);
    font-size: 40px; line-height: 1.05; text-align: center; letter-spacing: 0.5px;
  }
  .brand__tagline {
    margin-top: 14px; font-family: "Crimson Text", serif; font-style: italic;
    font-size: 17px; line-height: 1.2; color: var(--ink-soft); text-align: center;
  }

  .contact {
    position: absolute; top: 330px; left: 48px; right: 30px;
    font-family: "Poppins", sans-serif; color: var(--ink);
  }
  .contact__name { font-size: 22px; letter-spacing: 0.5px; }
  .contact__name strong { font-weight: 700; }
  .contact__name span { font-weight: 400; }
  .contact__title { font-size: 14px; letter-spacing: 2px; color: var(--ink-soft); margin-bottom: 18px; }
  .contact__line { font-size: 17px; line-height: 1.45; display: flex; align-items: center; gap: 10px; }
  .contact__line svg { flex: none; }
  .contact__address { margin-bottom: 4px; }

  .divisions {
    position: absolute; top: 546px; left: 40px; right: 30px;
    display: flex; justify-content: space-between; align-items: flex-end;
    font-family: "Poppins", sans-serif; font-weight: 600; font-size: 17px; line-height: 1.15;
  }
  .division { display: flex; flex-direction: column; align-items: center; text-align: center; }
  .division__mark { width: 38px; height: 38px; border-radius: 5px; margin-bottom: 8px; }
  .division--homecare { color: var(--coral); }
  .division--homecare .division__mark { background: var(--coral); }
  .division--living { color: var(--teal); }
  .division--living .division__mark { background: var(--teal); }

  .web-band {
    position: absolute; left: 0; right: 0; bottom: 0; height: 64px; background: var(--band);
    border-top: 6px solid var(--card-white); box-shadow: 0 -3px 0 var(--band);
    display: flex; align-items: center; justify-content: center;
    font-family: "Poppins", sans-serif; font-weight: 500; font-size: 18px; letter-spacing: 2px;
    color: var(--card-white);
  }

  .back-pattern {
    position: absolute; inset: 0;
    background: linear-gradient(135deg, var(--back-dark) 0%, var(--back-dark) 35%, var(--back-mid) 62%, var(--back-light) 100%);
  }
</style>
</head>
<body>
<main class="stage">
  <section class="card card--front" aria-label="Card front">
    <div class="brand">
      <div class="brand__mark"></div>
      <div class="brand__name">Brookfane<br>Care Group</div>
      <p class="brand__tagline">Someone you can depend on...<br>Without question.</p>
    </div>

    <div class="contact">
      <p class="contact__name"><strong>MARLA</strong> <span>DENHOLM</span></p>
      <p class="contact__title">PRESIDENT</p>
      <p class="contact__line contact__address">4870 Lanikai Ridge Rd., Suite 310<br>Halewai, HI 96722</p>
      <p class="contact__line">
        <svg width="18" height="18" viewBox="0 0 18 18" aria-hidden="true"><rect x="1" y="1" width="16" height="16" rx="2" fill="#111"/><rect x="5" y="5" width="8" height="8" fill="none" stroke="#fff" stroke-width="1.6"/></svg>
        (808) 555-0142
      </p>
      <p class="contact__line">
        <svg width="18" height="18" viewBox="0 0 18 18" aria-hidden="true"><rect x="1" y="1" width="16" height="16" rx="2" fill="#111"/><rect x="4" y="5.5" width="10" height="7" fill="none" stroke="#fff" stroke-width="1.2"/><path d="M4 5.5 9 10 14 5.5" fill="none" stroke="#fff" stroke-width="1.2"/></svg>
        Marla@BrookfaneCare.com
      </p>
    </div>

    <div class="divisions">
      <div class="division division--homecare">
        <div class="division__mark"></div>
        <span>Brookfane<br>Homecare</span>
      </div>
      <div class="division division--living">
        <div class="division__mark"></div>
        <span>Brookfane<br>Senior Living</span>
      </div>
    </div>

    <div class="web-band">www.BrookfaneCare.com</div>
  </section>

  <section class="card card--back" aria-label="Card back">
    <div class="back-pattern" role="img" aria-label="Repeating pattern of the company mark in glossy black fading to silver"></div>
  </section>
</main>
</body>
</html>
```